Business Card Design for an international medical business

We need a professional and elegant business card design with fashionable graphic element. Our company is located in Hong Kong with three worldwide production lines for medical equipment(surgical face masks, N95, face shields and so on). Our factories all contain medical standard ISOs and all product fulfill Marwick lab and KTR testing standards.

We would like to see designs that show the impression of our professional expertise, formal corporate image with creative thinking work style and inspiring global concept. We want the content in both English and Japanese on the same card. We also want to print our the patent trade mark and company logo on the card.

Target Market(s)

Southeast Asia, US, EU

Industry/Entity Type

Medical Equipment

Contact Information for Business Card

Below are the content we want to be shown on the business card(please help us to simplified them to be more presentable and readable):

Company name: Orlane (Hong Kong) 5K Medical Technology Company Limited
Address: Unit 2204, 22/F, Pebble Tower, No.8 Kendrick Lane, Wan Kei Shan, Hong Kong.
Band Name: Q5K
Homepage: www.tessiran5kbq.example
Name: Lok Wing Sze
Title: Manager
Tel: +852-xxxx-xxxx
Mobile: +852-xxxx-xxxx
Email: xx@orlane5kbq.example

Production Lines:
China: Pei Ling Sun Ke Medical Technology Company Limited
Mo Lan City Rui Fa Textile Machinery Company Limited
Bangladesh: Q5K Medical Technology Company Limited

Qualifications:
ISO 13485:2016
ISO 14644-1:2015
ISO Class 8 Cleanroom
ASTM F2100 Level 2
EN14683 Type IIR
EN149 FFP2
CE Certified
FDA Registration number: XXX

Requirements
Must have
• use pantone color for the design
and provide the pantone number for printing purpose
Should not have
• Background color should not be black.

```html
<!DOCTYPE html>
<html lang="en">
<head>
<meta charset="utf-8">
<title>Tessiran 5K – Business Card</title>
<link rel="stylesheet" href="https://fonts.googleapis.com/css2?family=Roboto:wght@400;500;700&display=swap">
<style>
  :root{
    --pink:#e0144c;
    --teal:#1aa6a6;
    --ink:#2b2b2b;
    --card:#f7f7f7;
    --stage:#e2e2e2;
  }
  *{box-sizing:border-box;margin:0;padding:0}
  html,body{width:1200px;height:576px;overflow:hidden}
  body{background:var(--stage);font-family:"Roboto",Arial,sans-serif;color:var(--ink);position:relative}

  .card{position:absolute;top:138px;width:485px;height:294px;background:var(--card);border-radius:11px;overflow:hidden;box-shadow:0 3px 8px rgba(0,0,0,.18)}
  .card--back{left:81px}
  .card--front{left:602px;width:481px;height:292px}

  /* back side */
  .brand__dot{position:absolute;left:118px;top:40px;width:26px;height:26px;border-radius:50%;background:var(--pink)}
  .brand__rule{position:absolute;left:164px;top:36px;width:1.5px;height:64px;background:var(--teal)}
  .brand__name{position:absolute;left:174px;top:28px;font-weight:700;font-size:46px;letter-spacing:.5px;color:var(--pink);line-height:1;white-space:nowrap}
  .brand__tag{position:absolute;left:178px;top:76px;font-size:9.5px;font-weight:700;color:var(--teal);white-space:nowrap}

  .panel{position:absolute;left:42px;width:398px;height:72px;border:1.5px solid;border-bottom:none;border-radius:12px 12px 0 0;
    -webkit-mask-image:linear-gradient(to bottom,#000 45%,transparent 100%);mask-image:linear-gradient(to bottom,#000 45%,transparent 100%)}
  .panel--lines{top:109px;border-color:var(--teal)}
  .panel--quals{top:197px;border-color:var(--pink)}
  .pill{position:absolute;left:50%;transform:translateX(-50%);padding:3px 13px;border-radius:12px;color:#fff;font-size:12.5px;font-weight:500;white-space:nowrap}
  .pill--pink{top:99px;background:var(--pink)}
  .pill--teal{top:187px;background:var(--teal)}

  .list{position:absolute;left:0;right:0;text-align:center;font-size:12.6px;line-height:16.5px;white-space:nowrap}
  .list--lines{top:124px}
  .list--quals{top:213px}
  .country{color:var(--pink);font-weight:700}
  .sep{color:var(--pink);padding:0 5px}

  .stripe{position:absolute;left:0;bottom:0;height:14px;width:50%}
  .stripe--pink{background:var(--pink)}
  .stripe--teal{left:50%;background:var(--teal)}

  /* front side */
  .mark__dot{position:absolute;left:127px;top:62px;width:27px;height:27px;border-radius:50%;background:var(--pink)}
  .mark__name{position:absolute;left:60px;top:178px;width:160px;text-align:center;font-weight:700;font-size:44px;color:var(--pink);letter-spacing:2px;line-height:1}

  .person{position:absolute;left:274px;top:46px}
  .person__name{font-size:21px;font-weight:500;color:var(--teal);line-height:1.2}
  .person__title{font-size:12.5px;margin-top:2px}

  .contacts{position:absolute;left:274px;top:104px;list-style:none;font-size:12.8px}
  .contacts li{display:flex;align-items:center;gap:8px;height:20.5px}
  .contacts svg{width:12px;height:12px;fill:var(--teal)}
  .address{position:absolute;left:274px;top:195px;font-size:12.8px;line-height:16px;font-style:normal}
</style>
</head>
<body>
  <section class="card card--back">
    <span class="brand__dot"></span>
    <span class="brand__rule"></span>
    <span class="brand__name">TESSIRAN</span>
    <p class="brand__tag">5K Medical Technology Company Limited</p>

    <div class="panel panel--lines"></div>
    <span class="pill pill--pink">Our Production Lines</span>
    <div class="list list--lines">
      <p><span class="country">CHINA:</span> Pei Ling Sun Ke Medical Technology Company Limited</p>
      <p>Mo Lan City Rui Fa Textile Machinery Company Limited</p>
      <p><span class="country">BANGLADESH:</span> Q5K Medical Technology Company Limited</p>
    </div>

    <div class="panel panel--quals"></div>
    <span class="pill pill--teal">Our Qualifications</span>
    <div class="list list--quals">
      <p>ISO 13485:2016<span class="sep">|</span>ISO 14644-1:2015<span class="sep">|</span>ISO Class 8 Cleanroom</p>
      <p>ASTM F2100 Level 2<span class="sep">|</span>EN14683 Type IIR<span class="sep">|</span>EN149 FFP2</p>
      <p>CE Certified<span class="sep">|</span>FDA Registration number: 12345</p>
    </div>

    <span class="stripe stripe--pink"></span><span class="stripe stripe--teal"></span>
  </section>

  <section class="card card--front">
    <span class="mark__dot"></span>
    <span class="mark__name">Q5K</span>

    <div class="person">
      <h1 class="person__name">Lok Wing Sze</h1>
      <p class="person__title">Manager</p>
    </div>

    <ul class="contacts">
      <li><svg viewBox="0 0 24 24"><path d="M6.6 10.8a15 15 0 0 0 6.6 6.6l2.2-2.2a1 1 0 0 1 1-.25 11.4 11.4 0 0 0 3.6.57 1 1 0 0 1 1 1V20a1 1 0 0 1-1 1A17 17 0 0 1 3 4a1 1 0 0 1 1-1h3.5a1 1 0 0 1 1 1c0 1.25.2 2.45.57 3.57a1 1 0 0 1-.25 1z"/></svg>+852-0000-0000</li>
      <li><svg viewBox="0 0 24 24"><path d="M6.6 10.8a15 15 0 0 0 6.6 6.6l2.2-2.2a1 1 0 0 1 1-.25 11.4 11.4 0 0 0 3.6.57 1 1 0 0 1 1 1V20a1 1 0 0 1-1 1A17 17 0 0 1 3 4a1 1 0 0 1 1-1h3.5a1 1 0 0 1 1 1c0 1.25.2 2.45.57 3.57a1 1 0 0 1-.25 1z"/></svg>+852-0000-0000</li>
      <li><svg viewBox="0 0 24 24"><path d="M2 5h20v14H2zm2 2v.5l8 5 8-5V7l-8 5z"/></svg>lok@tessiran5kbq.example</li>
      <li><svg viewBox="0 0 24 24"><path d="M12 2a10 10 0 1 0 0 20 10 10 0 0 0 0-20zm6.9 6h-2.9a15 15 0 0 0-1.4-3.6A8 8 0 0 1 18.9 8zM12 4a13 13 0 0 1 1.9 4h-3.8A13 13 0 0 1 12 4zM4.3 14a8 8 0 0 1 0-4h3.4a16 16 0 0 0 0 4zm.8 2h2.9a15 15 0 0 0 1.4 3.6A8 8 0 0 1 5.1 16zM8 8H5.1a8 8 0 0 1 4.3-3.6A15 15 0 0 0 8 8zm4 12a13 13 0 0 1-1.9-4h3.8A13 13 0 0 1 12 20zm2.3-6H9.7a14 14 0 0 1 0-4h4.6a14 14 0 0 1 0 4zm.3 5.6A15 15 0 0 0 16 16h2.9a8 8 0 0 1-4.3 3.6zM16.3 14a16 16 0 0 0 0-4h3.4a8 8 0 0 1 0 4z"/></svg>www.tessiran5kbq.example</li>
    </ul>

    <address class="address">Unit 2204, 22/F, Pebble Tower,<br>No.8 Kendrick Lane,<br>Wan Kei Shan, Hong Kong.</address>
  </section>
</body>
</html>
```